new marketing company logo and business card

design logo and biz card for marketing start up.

My company name needs a brand logo designed: Cedar Hollow Marketing Co.
Tagline: Sales - Marketing - Brand Building

Sister Bay is the name of my favorite place, in Wisconsin, but the business is NOT BASED there. It should evoke warmth, friendliness, professionalism, and marketing services from a seasoned marketer.

Target Market(s)

I am selling my services to small business that need help.

Industry/Entity Type

Marketing

Contact Information for Business Card

Cedar Hollow Marketing Co. (logo)
Sales - Marketing - Brand Building (tagline)

Maren T. Holloway
MarenTHolloway@quillpost.net
555-014-3926 mobile

Font styles to use
Serif
Sans Serif

Colors
f78f20
f37122
f68d4d
00a990
85cae6
33b8a4
faa54b

Requirements
Must have
• a logo
• a business card
Nice to have
• I'd love to see a small subtle reference to Sister Bay built in. Sister bay is named that because there are two islands called ‘sister islands’ that flank the bay. If you google this you will see.
• I like warm, earthy colors. But, I am a fun, approachable, real person. Not stand-offish. Should be warm and appealing yet professional.
Should not have
• nothing cartoon-ish. no child-like fonts. this is a professional business.

```html
<!DOCTYPE html>
<html lang="en">
<head>
<meta charset="utf-8">
<title>Cedar Hollow Marketing Co. — Business Card</title>
<link rel="stylesheet" href="https://fonts.googleapis.com/css2?family=Roboto:wght@500;700&family=Lato:wght@400&family=Montserrat:wght@600&display=swap">
<style>
  :root {
    --orange: #f37122;
    --teal: #33b8a4;
    --teal-dark: #00a990;
    --ink: #3a3a3a;
    --grey: #6d6d6d;
    --paper: #ffffff;
    --backdrop: #ecebe8;
  }
  * { margin: 0; padding: 0; box-sizing: border-box; }
  html, body { width: 1200px; height: 900px; overflow: hidden; }
  body { background: var(--backdrop); position: relative; }

  .card {
    position: absolute;
    background: var(--paper);
    overflow: hidden;
    box-shadow: 0 2px 6px rgba(0,0,0,.18);
  }
  .card--front { left: 330px; top: 90px; width: 555px; height: 343px; }
  .card--back  { left: 330px; top: 469px; width: 559px; height: 343px; }

  .card__waves { position: absolute; inset: 0; }

  .brand-dot {
    position: absolute;
    border-radius: 50%;
    background: var(--orange);
  }
  .card--front .brand-dot { left: 46px; top: 61px; width: 174px; height: 174px; }
  .card--back .brand-dot  { left: 67px; top: 104px; width: 134px; height: 134px; }

  .contact { position: absolute; left: 267px; top: 107px; }
  .contact__name {
    font: 700 20px/1 "Roboto", sans-serif;
    color: var(--teal-dark);
    letter-spacing: .2px;
    margin-bottom: 17px;
  }
  .contact__line {
    display: flex; align-items: center; gap: 6px;
    font: 400 16px/21px "Lato", sans-serif;
    color: var(--ink);
  }
  .contact__line svg { flex: none; fill: var(--teal-dark); }

  .tagline-band {
    position: absolute; right: 22px; bottom: 27px;
    font: 500 16px/1 "Roboto", sans-serif;
    color: #fff;
    letter-spacing: .3px;
  }

  .divider {
    position: absolute; left: 219px; top: 112px;
    width: 2px; height: 120px; background: #c9c9c9;
  }
  .wordmark { position: absolute; left: 240px; top: 134px; color: var(--teal); }
  .wordmark__name {
    font: 600 34px/1 "Montserrat", sans-serif;
    letter-spacing: .5px;
  }
  .wordmark__sub {
    font: 600 17px/1 "Montserrat", sans-serif;
    margin: 6px 0 0 44px;
  }
  .wordmark__tagline {
    position: absolute; left: 240px; top: 207px;
    font: 500 11px/1 "Roboto", sans-serif;
    letter-spacing: 1.6px;
    color: var(--grey);
  }
</style>
</head>
<body>

  <section class="card card--front">
    <div class="brand-dot" role="img" aria-label="Cedar Hollow Marketing Co. emblem"></div>

    <div class="contact">
      <p class="contact__name">MAREN T. HOLLOWAY</p>
      <p class="contact__line">
        <svg width="13" height="12" viewBox="0 0 24 22" aria-hidden="true"><path d="M3 8c0-3 4-5 9-5s9 2 9 5v2h-5V8H8v2H3zM6 11h12l3 9H3z"/></svg>
        555-014-3926
      </p>
      <p class="contact__line">
        <svg width="13" height="10" viewBox="0 0 26 18" aria-hidden="true"><path d="M0 0h26v18H0zM2 2v1l11 7 11-7V2z"/></svg>
        MarenTHolloway@quillpost.net
      </p>
    </div>

    <svg class="card__waves" viewBox="0 0 555 343" aria-hidden="true">
      <path d="M0 283 C160 292 350 225 555 247 L555 343 L0 343 Z" fill="var(--orange)"/>
      <path d="M0 252 C90 282 190 284 290 257 C190 272 90 274 0 266 Z" fill="var(--teal)"/>
    </svg>

    <p class="tagline-band">SALES - MARKETING - BRAND BUILDING</p>
  </section>

  <section class="card card--back">
    <div class="brand-dot" role="img" aria-label="Cedar Hollow Marketing Co. emblem"></div>
    <div class="divider"></div>
    <div class="wordmark">
      <p class="wordmark__name">CEDAR HOLLOW</p>
      <p class="wordmark__sub">MARKETING CO.</p>
    </div>
    <p class="wordmark__tagline">SALES | MARKETING | BRAND BUILDING</p>
  </section>

</body>
</html>
```